Webdesign für Automotive Engineering Webpage
Automotive Engineering - Main focus is Software Development & Embedded systems for the Automotive industry.
Like as HMI, ADAS, ECU
See Logo (PDF), example --> https://www.brantlex.com/de/de (competetor)

```html
<!DOCTYPE html>
<html lang="de">
<head>
<meta charset="utf-8">
<title>Valtrion – Automotive Engineering</title>
<link href="https://fonts.googleapis.com/css2?family=Lato:wght@400;700&family=Montserrat:wght@600;700&display=swap" rel="stylesheet">
<style>
:root{
  --red:#e3262b;
  --navy:#0d2d5e;
  --ink:#333a44;
  --text:#3c434d;
  --muted:#8f97a6;
  --line:#e4e7ee;
  --footer:#f4f5f9;
  --white:#fff;
}
*{box-sizing:border-box;margin:0;padding:0}
html,body{width:1200px;height:3241px;overflow:hidden;background:var(--white)}
body{position:relative;font-family:"Lato",sans-serif;color:var(--text)}
.abs{position:absolute}
h1,h2,h3{font-family:"Montserrat",sans-serif;font-weight:600}

/* header */
.site-header{left:0;top:0;width:1200px;height:86px;background:var(--white)}
.brand{left:100px;top:28px;font-family:"Montserrat",sans-serif;font-weight:700;font-size:24px;color:var(--navy);letter-spacing:1px;display:flex;align-items:center;gap:8px}
.brand-dot{width:10px;height:10px;border-radius:50%;background:var(--red)}
.main-nav{left:420px;top:32px;display:flex;gap:18px;font-size:12px;letter-spacing:1.6px;color:var(--ink);align-items:center}
.main-nav .active{background:var(--red);color:var(--white);padding:4px 14px;clip-path:polygon(10px 0,100% 0,calc(100% - 10px) 100%,0 100%)}
.lang{left:1068px;top:34px}

/* hero */
.hero{left:0;top:86px;width:1200px;height:600px;background:linear-gradient(100deg,#1b1e22 0%,#2b3138 40%,#5a5e64 68%,#3a3e44 85%,#23272c 100%)}
.hero-title{left:100px;top:226px;font-size:45px;line-height:56px;color:var(--white);font-weight:700}
.hero-text{left:100px;top:372px;width:320px;font-size:13px;line-height:18px;color:var(--white)}
.btn{display:inline-block;background:var(--red);color:var(--white);font-size:12px;letter-spacing:1.6px;padding:6px 10px;border-radius:2px}
.hero-btn{left:100px;top:442px}
.hero-social{left:106px;top:604px;display:flex;gap:22px}
.hero-social span{width:24px;height:24px;border:2px solid #7b8088;border-radius:4px}

/* sections */
.section-title{width:1200px;text-align:center;color:var(--ink);font-size:28px}
.tabs{left:0;top:846px;width:1200px;display:flex;justify-content:center;gap:10px;font-size:14px;letter-spacing:2px;color:var(--ink);align-items:center}
.tabs .active{background:var(--red);color:var(--white);padding:4px 22px;clip-path:polygon(10px 0,100% 0,calc(100% - 10px) 100%,0 100%)}
.photo{background:linear-gradient(160deg,#b9c0c8,#7d8894)}
.service-title{left:416px;top:952px;font-size:24px;color:var(--ink)}
.copy{font-size:11.5px;line-height:18.5px;color:var(--text)}
.bullets{left:416px;top:1104px;width:620px;list-style:none}
.bullets li{position:relative;padding-left:26px;margin-bottom:26px}
.bullets li::before{content:"";position:absolute;left:6px;top:6px;width:7px;height:7px;border-radius:50%;background:var(--red)}
.bullets strong{display:block;margin-top:7px;font-weight:700;color:#22272e}
.divider{left:100px;width:1000px;height:4px;background:var(--line)}
.about-copy{left:540px;top:1718px;width:500px;font-size:13.2px;line-height:18.5px}
.about-copy p+p{margin-top:18px}

/* blog */
.feature{left:198px;top:2305px;width:393px;height:256px;background:linear-gradient(150deg,#d8403a,#7a2a25 55%,#3b3b3b);box-shadow:0 10px 22px rgba(0,0,0,.22)}
.feature-band{position:absolute;left:0;bottom:0;width:100%;height:80px;background:rgba(227,38,43,.92);padding:26px 25px}
.feature-band h3{font-family:"Lato",sans-serif;font-weight:700;font-size:14px;color:var(--white)}
.date{font-size:11px;letter-spacing:2px;color:var(--muted);margin-top:6px}
.feature-band .date{color:#ffd9da}
.post-title{font-size:13px;color:var(--ink)}

/* newsletter */
.newsletter{left:0;top:2648px;width:1200px;height:328px;background:var(--navy);overflow:hidden}
.newsletter h2{position:absolute;top:100px;width:1200px;text-align:center;color:var(--white);font-size:28px;font-weight:700}
.newsletter p{position:absolute;top:146px;width:1200px;text-align:center;color:#dfe6f2;font-size:13px;line-height:19px}
.email{position:absolute;left:435px;top:203px;width:207px;height:39px;background:var(--white);border-radius:2px;font-size:12px;color:#a0a7b4;padding:12px}
.subscribe{position:absolute;left:650px;top:203px;width:114px;height:39px;background:var(--red);color:var(--white);font-size:12px;letter-spacing:1.6px;text-align:center;line-height:39px}

/* footer */
.site-footer{left:0;top:2976px;width:1200px;height:265px;background:var(--footer)}
.footer-links{left:391px;top:3031px;list-style:none;font-size:13px;color:var(--muted);line-height:26.5px}
.contact{font-size:11.5px;color:var(--muted);line-height:17px}
.footer-social{left:980px;top:3030px;display:flex;gap:22px}
.footer-social span{width:26px;height:26px;border-radius:50%;background:var(--navy)}
.copyright{left:0;top:3202px;width:1200px;text-align:center;font-size:11px;color:var(--muted)}
</style>
</head>
<body>

<header class="site-header abs">
  <div class="brand abs"><span class="brand-dot"></span>VALTRION</div>
  <nav class="main-nav abs">
    <span class="active">HOME</span><span>LEISTUNGEN</span><span>UBER UNS</span><span>KONTAKT US</span>
  </nav>
  <svg class="lang abs" width="32" height="16" viewBox="0 0 32 16" fill="none" stroke="#e3262b" stroke-width="1.4">
    <circle cx="8" cy="8" r="7"/><ellipse cx="8" cy="8" rx="3" ry="7"/><line x1="1" y1="8" x2="15" y2="8"/>
    <polyline points="20,6 23,9 26,6"/>
  </svg>
</header>

<section class="hero abs" role="img" aria-label="White sports car parked in a dim industrial hall"></section>
<h1 class="hero-title abs">Choosing<br>The Right Path</h1>
<p class="hero-text abs">The harder you work for something, the greater you'll feel when you achieve it.</p>
<span class="btn hero-btn abs">LEARN MORE</span>
<div class="hero-social abs" aria-label="Social links"><span></span><span></span><span></span></div>

<h2 class="section-title abs" style="left:0;top:776px">Unsere Geschäftsbereiche</h2>
<div class="tabs abs"><span>FULL SERVICE ENGINEERING</span><span class="active">PREMIUM RECRUITING</span><span>TEMPING</span></div>

<div class="photo abs" style="left:100px;top:959px;width:256px;height:303px" role="img" aria-label="Engineer standing in front of an office building"></div>

<h3 class="service-title abs">Premium Recruiting</h3>
<p class="copy abs" style="left:416px;top:1000px;width:684px">Drängen Projekte? Fehlen Fachleute? Ist das klassische Recruitment Outsourcing zu zeitaufwändig und zu ungenau? Wir sind nicht einfach nur Personaldienstleister, sondern vielmehr Lösungsanbieter, auf Wunsch bis hin zum Onboarding! Nicht Sie wälzen irgendwelche Profile, sondern wir qualifizieren vor und präsentieren Ihnen wenige, passgenaue Kandidaten – mit durchschnittlich 80% Trefferquote!</p>
<ul class="bullets abs copy">
  <li>Wir stellen Ihnen einzelne Experten oder auch ganze Teams zur Verfügung, die auf Anhieb passen, denn wir verfügen über persönliche, jahrzehntelange Erfahrung als Ingenieure im Automotive Sektor sowie in anderen Hightech Schlüsselindustrien. Sie entscheiden, in welcher Form die Zusammenarbeit stattfinden soll!<strong>Wir kennen Ihre Anforderungen und haben flexible Lösungen dafür!</strong></li>
  <li>Wir verfügen über großes Netzwerk an IT-Spezialisten, R&amp;D Ingenieuren und Key-Managern aus den genannten Industrien. Unser Pool ist handverlesen und in der Praxis erprobt!<strong>Wir haben die Experten, die den geforderten Ansprüchen gerecht werden!</strong></li>
  <li>Wir verfolgen einen auf Effizienz ausgerichteten, kurzen Auswahl-Prozess mit wenigen, bereits konkreten und passgenauen Vorschlägen für die richtigen Mitarbeiter oder für ganze Teams bis hin zum durch uns durchgeführten Projekt Boarding. Wir vermeiden unnötige Reibungsverluste und kommen schnell in die Umsetzung!<strong>Wir sparen Ihre Zeit und Ihr Geld!</strong></li>
</ul>

<div class="divider abs" style="top:1519px"></div>

<h2 class="section-title abs" style="left:0;top:1612px">Wer Wir Sind</h2>
<div class="photo abs" style="left:162px;top:1720px;width:326px;height:317px;background:linear-gradient(150deg,#c9ced6,#5c6470 60%,#2c3138)" role="img" aria-label="Three engineers working at a laptop beside a vehicle test rig"></div>
<div class="about-copy abs">
  <p>Halvorn Recruitment vereint in sich 25 Jahre Branchen- und Projekterfahrung vom Freelance Ingenieur bis zum Task Force Manager in den Branchen Automotive, Schienenfahrzeuge, Luft- und Raumfahrt, Rüstung und Informationstechnologie.</p>
  <p>Firmengründer und Geschäftsführer Jonas Halvorn kennt die Industrie seit über zwei Jahrzehnten, in denen er in Positionen als IT Entwicklungsingenieur, Experte für Geodaten und rund um das Thema autonomes Fahren und Fahrassistenzsysteme, bis zum CIO und Task Force Manager bei fast allen wichtigen OEMs und Tier1s des Automotive Sektors und anderer Schlüsselindustrien Erfahrungen sammeln konnte.</p>
</div>
<span class="btn abs" style="left:540px;top:1908px">READ MORE</span>

<div class="divider abs" style="top:2145px"></div>

<h2 class="section-title abs" style="left:0;top:2238px">Blog</h2>
<article class="feature abs" role="img" aria-label="Close-up of a red engine bay with air filters">
  <div class="feature-band"><h3>The Best Sales Prospect Engine</h3><div class="date">FEB 2</div></div>
</article>
<div class="photo abs" style="left:609px;top:2305px;width:188px;height:136px;background:linear-gradient(180deg,#b59a78,#6e6660 60%,#3a3a3c)" role="img" aria-label="Dark sports car in front of a wooden wall"></div>
<div class="post-title abs" style="left:609px;top:2459px">Viverra Accumsan Tellus</div>
<div class="date abs" style="left:609px;top:2484px">JAN 31</div>
<div class="photo abs" style="left:814px;top:2305px;width:189px;height:136px;background:linear-gradient(160deg,#6b6f74,#2a2c30 60%,#151617)" role="img" aria-label="Gear shift lever in a car interior"></div>
<div class="post-title abs" style="left:814px;top:2459px">Unlock Calls</div>
<div class="date abs" style="left:814px;top:2484px">JAN 15</div>

<section class="newsletter abs">
  <h2>Newsletter</h2>
  <p>Failure will never overtake me if my determination to<br>succeed is strong enough.</p>
  <div class="email">Your email</div>
  <div class="subscribe">ABONNIEREN</div>
</section>

<footer class="site-footer abs"></footer>
<div class="brand abs" style="top:3052px;font-size:30px"><span class="brand-dot"></span>VALTRION</div>
<ul class="footer-links abs"><li>Kontakt</li><li>AGB</li><li>Impressum</li><li>Datenschutz</li><li>Updates</li></ul>
<svg class="abs" style="left:662px;top:3032px" width="12" height="16" viewBox="0 0 12 16"><path d="M6 0a6 6 0 0 0-6 6c0 4.5 6 10 6 10s6-5.5 6-10a6 6 0 0 0-6-6z" fill="#0d2d5e"/><circle cx="6" cy="6" r="2.2" fill="#f4f5f9"/></svg>
<div class="contact abs" style="left:686px;top:3033px">418 Lindqvist Avenue,<br>Suite 5120, Marlow Bay, GA<br>900117</div>
<svg class="abs" style="left:661px;top:3100px" width="14" height="14" viewBox="0 0 14 14"><path d="M3 0l3 3-1.6 2.2a8 8 0 0 0 4.4 4.4L11 8l3 3-2 2.6C6 13 1 8 .4 2z" fill="#0d2d5e"/></svg>
<div class="contact abs" style="left:686px;top:3099px">+1 555 010246</div>
<svg class="abs" style="left:661px;top:3136px" width="15" height="11" viewBox="0 0 15 11"><rect width="15" height="11" fill="#0d2d5e"/><polyline points="1,1 7.5,6 14,1" fill="none" stroke="#f4f5f9" stroke-width="1.4"/></svg>
<div class="contact abs" style="left:686px;top:3133px">hello@valtrion.kit</div>
<div class="footer-social abs" aria-label="Social links"><span></span><span></span><span></span></div>
<div class="copyright abs">Copyright © 2020. All rights reserved.</div>

</body>
</html>
```